Car rental website design for a UAE car rental company

This project is about creating a new website design for a car rental company located in Dubai (United Arab Emirates), I opened the same project a few months ago but I didn't receive a lot of appealing entries so I closed it but this time I am marking the project as guaranteed to avoid such situation again, if you have already provided a design before then please re-submit again on this project so that it is considered while reviewing all the designs

A few important things:

1- We need a simple non-complex design
2- The final deliverable would be 2 screens (PSD, JPEG ... etc), the first screen is for the home page and the second screen is for an internal page
3- The home page must have a section that end users can use to rent a car online directly from the home page instead of going into some inner pages
4- The current website is very old and not very appealing so avoid creating a similar design (www.quarvin-drive.example)
5- The name is Quarvin but the company rents normal cars (no Limousin cars will be rented) so avoid adding any fancy cars in the images/graphics used in the design, just normal end users cars
6- The expected pages would be: home, About us, Our team, Strategy, Contact us and links to social media pages
7- The attachments include the company's logo and some screens from other car rental companies that provide online rentals/payments

If you have any questions please feel free to ask and please note that we will need the designs urgently

Thanks

Target Market(s)

Dubai - United Arab Emirates

Industry/Entity Type

It Company

Number of Pages Required

2 page

Font styles to use
Sans Serif

Requirements
Must have
• Check the project details
Nice to have
Should not have

```html
<!DOCTYPE html>
<html lang="en">
<head>
<meta charset="utf-8">
<title>Quarvin Rent A Car</title>
<link href="https://fonts.googleapis.com/css2?family=Arimo:wght@400;700&display=swap" rel="stylesheet">
<style>
:root{
  --crimson:#a3163b;
  --crimson-dark:#7e0f2c;
  --crimson-soft:#b71d47;
  --ink:#222;
  --ink-soft:#3a3a3a;
  --card:#f4f4f4;
  --field:#f6f6f6;
  --field-line:#d6d6d6;
  --white:#fff;
  --logo-grey:#7d8a80;
}
*{margin:0;padding:0;box-sizing:border-box}
html,body{width:1071px;height:1200px;overflow:hidden;background:var(--white)}
body{font-family:"Arimo",Arial,sans-serif;color:var(--ink);position:relative}

.site-header{position:absolute;left:0;top:0;width:1071px;height:86px;background:var(--white)}
.brand{position:absolute;left:89px;top:0;width:153px;height:113px;background:var(--white);z-index:3;
  display:flex;flex-direction:column;align-items:center;justify-content:center;gap:10px}
.brand-mark{width:34px;height:34px;border:3px solid var(--crimson)}
.brand-name{font-size:22px;font-weight:700;color:var(--logo-grey)}
.call-now{position:absolute;right:98px;top:24px;font-size:12px;font-weight:700;color:var(--crimson)}
.main-nav{position:absolute;right:97px;top:52px;display:flex;gap:14px;font-size:12px;font-weight:700;white-space:nowrap}
.main-nav a{color:var(--ink);text-decoration:none}
.main-nav a.is-active{color:var(--crimson)}

.intro-band{position:absolute;left:0;top:86px;width:1071px;height:411px;
  background:radial-gradient(ellipse at 50% 40%,var(--crimson-soft) 0%,var(--crimson) 55%,var(--crimson-dark) 100%)}
.hero-slide{position:absolute;left:89px;top:32px;width:894px;height:269px;background:var(--white);
  border-bottom:3px solid #3b2a2f}
.hero-title{position:absolute;left:34px;top:30px;font-size:21px;font-weight:700;color:var(--ink-soft)}
.booking-form{position:absolute;left:34px;top:70px;width:380px;display:grid;grid-template-columns:1fr 1fr;gap:8px 12px}
.booking-field{display:flex;flex-direction:column;gap:3px;font-size:11px;font-weight:700;color:var(--ink-soft)}
.booking-field input{height:28px;border:1px solid var(--field-line);background:var(--field);padding:0 8px;
  font:400 12px "Arimo",Arial,sans-serif;color:var(--ink)}
.hero-button{grid-column:1 / span 2;width:192px;height:34px;margin-top:6px;background:var(--crimson);border:0;
  color:var(--white);font:400 12px "Arimo",Arial,sans-serif;border-radius:2px}
.slide-dots{position:absolute;left:34px;top:240px;display:flex;gap:4px}
.slide-dots span{width:9px;height:9px;border-radius:50%;background:#111}
.slide-dots span.is-current{background:var(--crimson)}
.hero-car{position:absolute;left:435px;top:37px;width:428px;height:190px;border-radius:40% 45% 20% 20%;
  background:radial-gradient(ellipse at 50% 45%,#e0222d 0%,#b3141c 55%,rgba(255,255,255,0) 75%)}
.intro-title{position:absolute;left:0;top:318px;width:100%;text-align:center;color:var(--white);font-size:22px;font-weight:400}
.intro-text{position:absolute;left:0;top:351px;width:100%;text-align:center;color:var(--white);font-size:13px;line-height:16px}

.featured{position:absolute;left:0;top:497px;width:1071px;height:610px;
  background:linear-gradient(100deg,#8ba65a 0%,#b7c98e 22%,#8e9a86 42%,#6f716f 62%,#2d2d2f 82%,#1c1c1e 100%)}
.featured-title{position:absolute;left:0;top:26px;width:100%;text-align:center;color:var(--white);
  font-size:20px;font-weight:700;text-shadow:0 1px 3px rgba(0,0,0,.5)}
.car-card{position:absolute;top:68px;width:280px;height:494px;background:var(--card)}
.car-card:nth-of-type(1){left:89px}
.car-card:nth-of-type(2){left:397px}
.car-card:nth-of-type(3){left:705px}
.card-title{position:absolute;left:17px;top:25px;font-size:12px;font-weight:700}
.car-photo{position:absolute;left:17px;top:49px;width:246px;height:133px;background:var(--white)}
.car-photo::after{content:"";position:absolute;left:15px;top:22px;width:216px;height:92px;border-radius:45% 45% 25% 25%;background:var(--tone)}
.price-bar{position:absolute;left:15px;top:184px;width:250px;height:43px;background:var(--crimson);color:var(--white);
  font-size:12px;font-weight:700;display:flex;justify-content:space-between;align-items:center;padding:0 10px 0 16px}
.spec-list{position:absolute;left:17px;top:237px;width:246px;list-style:none;font-size:12px;font-weight:700}
.spec-list li{height:27px;display:flex;align-items:center}
.spec-list li span:first-child{width:206px}
.card-button{position:absolute;left:48px;top:434px;width:184px;height:40px;background:var(--crimson);color:var(--white);
  font-size:12px;font-weight:700;display:flex;align-items:center;justify-content:center}

.site-footer{position:absolute;left:0;top:1107px;width:1071px;height:93px;background:var(--white)}
.copyright{position:absolute;left:100px;top:40px;font-size:10px;color:var(--ink)}
.social{position:absolute;right:89px;top:36px;display:flex;gap:18px}
.social span{width:20px;height:20px;border-radius:50%;background:#d9302c}
</style>
</head>
<body>
<header class="site-header">
  <div class="brand"><span class="brand-mark"></span><span class="brand-name">Quarvin</span></div>
  <div class="call-now">Call Now: 120.555.409</div>
  <nav class="main-nav">
    <a class="is-active" href="#">Home</a><a href="#">About us</a><a href="#">Our team</a><a href="#">Strategy</a><a href="#">Car Traveler</a><a href="#">Vehicles</a><a href="#">Locations</a><a href="#">My Bookings</a><a href="#">Help</a><a href="#">Contact us</a>
  </nav>
</header>

<section class="intro-band">
  <div class="hero-slide">
    <h1 class="hero-title">We Are A Car Rental Company</h1>
    <form class="booking-form" action="#">
      <label class="booking-field">Pick-up location<input type="text" value="Dubai Airport"></label>
      <label class="booking-field">Drop-off location<input type="text" value="Dubai Marina"></label>
      <label class="booking-field">Pick-up date<input type="text" value="12 / 06 / 2015"></label>
      <label class="booking-field">Return date<input type="text" value="15 / 06 / 2015"></label>
      <button class="hero-button" type="submit">A booking from to rent a car</button>
    </form>
    <div class="slide-dots"><span class="is-current"></span><span></span><span></span><span></span></div>
    <div class="hero-car" role="img" aria-label="Red sedan car photo"></div>
  </div>
  <h2 class="intro-title">Quarvin rent a car</h2>
  <p class="intro-text">Lorem ipsum dolor sit amet, consectetur adipiscing elit, sed do eiusmod tempor incididunt ut labore et dolore magna aliqua.<br>Ut enim ad minim veniam, quis nostrud exercitation ullamco laboris nisi ut aliquip ex ea commodo consequat.</p>
</section>

<section class="featured" role="img" aria-label="Background photo of a car driving on a blurred road">
  <h2 class="featured-title">Featured Cars</h2>

  <article class="car-card">
    <h3 class="card-title">Featured Car 1</h3>
    <div class="car-photo" role="img" aria-label="White convertible car photo" style="--tone:radial-gradient(ellipse,#e6e6e6 0%,#c9c9c9 55%,#fff 75%)"></div>
    <div class="price-bar"><span>Pris per døgn</span><span>Kr 600</span></div>
    <ul class="spec-list">
      <li><span>BiltypeVarebil</span><span>Varebil</span></li>
      <li><span>Maks. pers</span><span>2</span></li>
      <li><span>Ant. dører</span><span>5</span></li>
      <li><span>Min. sjåføralder</span><span>21</span></li>
      <li><span>Girtype</span><span>II</span></li>
      <li><span>Klimaanlegg?</span><span>Ja</span></li>
      <li><span>Ubegrenset km?</span><span>Nei</span></li>
    </ul>
    <div class="card-button">Read More About The Car</div>
  </article>

  <article class="car-card">
    <h3 class="card-title">Featured Car 1</h3>
    <div class="car-photo" role="img" aria-label="Red hatchback car photo" style="--tone:radial-gradient(ellipse,#e0302a 0%,#b41d1a 55%,#fff 75%)"></div>
    <div class="price-bar"><span>Pris per døgn</span><span>Kr 600</span></div>
    <ul class="spec-list">
      <li><span>BiltypeVarebil</span><span>Varebil</span></li>
      <li><span>Maks. pers</span><span>2</span></li>
      <li><span>Ant. dører</span><span>5</span></li>
      <li><span>Min. sjåføralder</span><span>21</span></li>
      <li><span>Girtype</span><span>II</span></li>
      <li><span>Klimaanlegg?</span><span>Ja</span></li>
      <li><span>Ubegrenset km?</span><span>Nei</span></li>
    </ul>
    <div class="card-button">Read More About The Car</div>
  </article>

  <article class="car-card">
    <h3 class="card-title">Featured Car 1</h3>
    <div class="car-photo" role="img" aria-label="Orange sports car photo" style="--tone:radial-gradient(ellipse,#f39323 0%,#e06f10 55%,#fff 75%)"></div>
    <div class="price-bar"><span>Pris per døgn</span><span>Kr 600</span></div>
    <ul class="spec-list">
      <li><span>BiltypeVarebil</span><span>Varebil</span></li>
      <li><span>Maks. pers</span><span>2</span></li>
      <li><span>Ant. dører</span><span>5</span></li>
      <li><span>Min. sjåføralder</span><span>21</span></li>
      <li><span>Girtype</span><span>II</span></li>
      <li><span>Klimaanlegg?</span><span>Ja</span></li>
      <li><span>Ubegrenset km?</span><span>Nei</span></li>
    </ul>
    <div class="card-button">Read More About The Car</div>
  </article>
</section>

<footer class="site-footer">
  <p class="copyright">Copyright© quarvin-drive.example,2015, All Right Reserved.</p>
  <div class="social"><span aria-label="Social link"></span><span aria-label="Social link"></span></div>
</footer>
</body>
</html>
```